new business card, with new logo. Looking for full design

I would like to have a graphic designer/artist create a high standard, premium business logo and business card design that I can either use to print on my own or have printed through them as well. Also, would be nice if I could customize with new employee names and info afterwards. Also, though I don't have a logo, something that matches the theme here https://veridanstrategy.com/ as well as incorporates the letter "M" is what I am currently thinking. Thanks!

Target Market(s)

High end corporate executives

Industry/Entity Type

Economics

Contact Information for Business Card

Dr. Tomas Ruelle-Brandt
Principal Advisor
TRB@VeridanStrategy.com
other contact/website details from here: https://veridanstrategy.com/

Logo Text

Veridan Strategy Group

```html
<!DOCTYPE html>
<html lang="en">
<head>
<meta charset="utf-8">
<title>Veridan Strategy Group — Business Card</title>
<link href="https://fonts.googleapis.com/css2?family=Barlow:wght@400;500;600&display=swap" rel="stylesheet">
<style>
  :root {
    --backdrop: #0e1a22;
    --card-dark: #333333;
    --card-light: #ffffff;
    --ink: #2b2b2b;
    --ink-muted: #7a7a7a;
    --ink-soft: #8c8c8c;
    --logo-on-dark: #4a4a4c;
    --rule-on-dark: #e6e6e6;
    --text-on-dark: #f2f2f2;
  }
  * { box-sizing: border-box; margin: 0; padding: 0; }
  html, body {
    width: 1200px; height: 797px; overflow: hidden;
    background: var(--backdrop);
    font-family: "Barlow", sans-serif;
  }
  .sheet {
    width: 1200px; height: 797px;
    display: flex; flex-direction: column;
    align-items: center; justify-content: center; gap: 36px;
  }
  .card {
    position: relative;
    width: 600px; height: 343px;
    overflow: hidden;
  }
  .card--back { background: var(--card-dark); }
  .card--front { background: var(--card-light); }

  /* wordmark */
  .wordmark {
    position: absolute;
    display: flex; align-items: center; gap: 12px;
    padding-bottom: 8px;
    border-bottom: 1.5px solid currentColor;
  }
  .wordmark__mark { width: 22px; height: 22px; background: currentColor; flex: none; }
  .wordmark__name {
    font-weight: 600; font-size: 21px; letter-spacing: 3px;
    text-transform: uppercase; white-space: nowrap;
  }
  .card--back .wordmark { color: var(--logo-on-dark); left: 50%; top: 105px; transform: translateX(-50%); }
  .card--front .wordmark { color: var(--ink); right: 40px; top: 46px; }

  .front-rule {
    position: absolute; right: 40px; top: 118px;
    width: 300px; height: 1.5px; background: var(--ink);
  }

  /* back: website band */
  .web-band {
    position: absolute; left: 0; right: 0; bottom: 88px;
    display: flex; align-items: center; gap: 14px; padding: 0 40px;
  }
  .web-band__rule { flex: 1; height: 1.5px; background: var(--rule-on-dark); }
  .web-band__url { color: var(--text-on-dark); font-size: 14px; font-weight: 500; letter-spacing: 0.6px; }

  /* front: person + contacts */
  .person { position: absolute; left: 40px; top: 188px; }
  .person__name { font-size: 25px; font-weight: 500; color: var(--ink); line-height: 1.1; }
  .person__role { font-size: 21px; font-weight: 500; color: var(--ink-muted); line-height: 1.2; }
  .contact-rule {
    position: absolute; left: 40px; right: 40px; top: 256px;
    height: 1.5px; background: var(--ink);
  }
  .contacts {
    position: absolute; left: 40px; top: 266px;
    display: grid; grid-template-columns: auto auto; column-gap: 26px; row-gap: 6px;
    font-size: 13px; color: var(--ink-soft); letter-spacing: 0.3px;
  }
  .contacts__item { display: flex; align-items: center; gap: 6px; white-space: nowrap; }
  .contacts__item--wide { grid-column: 1 / 3; }
  .contacts__icon { width: 12px; height: 12px; flex: none; }
</style>
</head>
<body>
<main class="sheet">
  <section class="card card--back" aria-label="Card back">
    <div class="wordmark">
      <span class="wordmark__mark"></span>
      <span class="wordmark__name">Veridan Strategy Group</span>
    </div>
    <div class="web-band">
      <span class="web-band__rule"></span>
      <span class="web-band__url">www.veridanstrategy.com</span>
      <span class="web-band__rule"></span>
    </div>
  </section>

  <section class="card card--front" aria-label="Card front">
    <div class="wordmark">
      <span class="wordmark__mark"></span>
      <span class="wordmark__name">Veridan Strategy Group</span>
    </div>
    <div class="front-rule"></div>

    <div class="person">
      <p class="person__name">Your Name here</p>
      <p class="person__role">Position</p>
    </div>
    <div class="contact-rule"></div>
    <div class="contacts">
      <p class="contacts__item contacts__item--wide">
        <svg class="contacts__icon" viewBox="0 0 12 12" fill="none" stroke="#8c8c8c" stroke-width="1.2"><path d="M6 11 C3 7.5 2.5 6 2.5 4.5 A3.5 3.5 0 0 1 9.5 4.5 C9.5 6 9 7.5 6 11Z"/><circle cx="6" cy="4.5" r="1.2"/></svg>
        2210 Harbor Crest ave # B48 Seabright Ca 90410
      </p>
      <p class="contacts__item">
        <svg class="contacts__icon" viewBox="0 0 12 12" fill="none" stroke="#8c8c8c" stroke-width="1.2"><circle cx="6" cy="6" r="5"/><path d="M4.2 3.5 L5 5 L4.6 5.6 Q5.5 7 6.6 7.5 L7.2 7 L8.5 7.8 L8 8.8 Q5 8.8 3.4 4.3Z"/></svg>
        123 555-0147
      </p>
      <p class="contacts__item">
        <svg class="contacts__icon" viewBox="0 0 12 12" fill="none" stroke="#8c8c8c" stroke-width="1.2"><circle cx="6" cy="6" r="2"/><path d="M8 6 V7 A1.5 1.5 0 0 0 11 7 V6 A5 5 0 1 0 8.5 10.3"/></svg>
        Name@veridanstrategy.com
      </p>
    </div>
  </section>
</main>
</body>
</html>
```